Marlow Landscaping Landing Page

I require a landing page for my landscaping business.

My business plan revolves around hooking clients with weeding services. Not lawn herbicide sprays, but actual hand weeding and bed maintenance. I've found my niche as most people do not want to do this kind of work. From there I often upsell clients into actual hardscaping or softscaping.

I like things to be clean, concise, and to the point. Not overly flashy, but not so minimal that that it's boring. My logo is a very good example of what I like.

The business is LGBTQ owned and operated. I do not broadcast this but I feel the logo itself, along with the name is usually enough to tip people into assumption. I'm not opposed to color, but I do not want the page to scream "gay". My favourite color is yellow...

I used to be a door to door salesman so I'm doing something different where I want to do all my selling in my first meeting with the client. With this said I do not need a section for "work pictures", as I have photos of my work on my tablet, which I show the client during the consultation.

Ideally i'd like my web site to actually be just a landing page. I'd like room for all the following information within the page;

- description of services;
Weeding of Perennial and Flower Beds
Selective Pruning of Trees and Shrubs
Hedging
Landscape Construction
Landscape Design
Total Lawn Treatment Plans
Landscape Pest Control

- contact information, phone, email
Gerald Hanswick
204-731-4426
ger.hanswick@brelvanyard.com

- "free estimates" somewhere on the page that is either led to by the eye, or very easy to notice and see

- and my slogan which is "dependable, reliable, consistent"

- room for a link to my future ratewell account so they can see reviews from real people

- My Logo present

Any or all of these can be custom made graphics or simply text, whatever looks best

I do not want people to have to search for information throughout. Design it in such a way that either the eye flows naturally from one piece of information to the other, or that it's all compartmentalized neatly enough that everything is easy to find.

As I am a landscape and outdoor maintenance service I'm no opposed to images such as flowers, trees, landscaping, etc being present. However please note that my main focus and source of income comes from weeding services, everything else is bonus cash.

Many of my clients are extremely wealthy individuals who pay over $1000 for the season for me just to show up and pull weeds. So making the website appeal to wealthy people as opposed to the average joe is paramount.

I do not cut grass. Please do not have any indication on the website, either through writing or graphics that implies that I cut grass. There are enough companies doing that.

Target Market(s)

Wealthy, often elderly individuals.

Industry/Entity Type

Landscape Gardening

Coding

Coded - Design and coding required

Number of Pages Required

1 page

Font styles to use
Sans Serif

Colors

Designer to choose colors to be used in the design.

Requirements
Must have
• - description of services;
• Weeding of Perennial and Flower Beds
• Selective Pruning of Trees and Shrubs
• Hedging
• Landscape Construction
• Landscape Design
• Total Lawn Treatment Plans
• Landscape Pest Control
• - contact information, phone, email
• Gerald Hanswick
• 204-731-4426
• ger.hanswick@brelvanyard.com
• - "free estimates" somewhere on the page that is either led to by the eye, or very easy to notice and see
• - and my slogan which is "dependable, reliable, consistent"
• - room for a link to my future ratewell account so they can see reviews from real people
• - My Logo present
Nice to have
• Flowers or weeds depicted. Possibly some hardscaping and softscaping if it doesnt look too bulky and crowded.
Should not have
• grass

```html
<!DOCTYPE html>
<html lang="en">
<head>
<meta charset="utf-8">
<title>Marlow Landscaping</title>
<link href="https://fonts.googleapis.com/css2?family=Open+Sans:wght@300;400;600;700&display=swap" rel="stylesheet">
<style>
:root{
  --yellow:#e5bf13;
  --yellow-dark:#b3930a;
  --ink:#2b2b2b;
  --body:#555;
  --muted:#8a8a8a;
  --line:#dcdcdc;
  --white:#fff;
  --footer:#2e2e2e;
  --nav-muted:#f6e7a8;
}
*{margin:0;padding:0;box-sizing:border-box}
html,body{width:1200px;height:4276px;overflow:hidden}
body{font-family:"Open Sans",Arial,sans-serif;color:var(--body);background:var(--white);position:relative}
.abs{position:absolute}

/* brand + navigation */
.brand{position:absolute;left:57px;font-size:20px;font-weight:700;letter-spacing:.5px;display:flex;align-items:center;gap:10px;line-height:30px}
.brand-square{width:14px;height:14px;display:inline-block}
.nav{position:absolute;top:0;height:100%;left:700px;right:40px;display:flex;justify-content:flex-end;align-items:center;gap:58px;font-size:14px;letter-spacing:.5px;text-transform:uppercase}
.nav a{text-decoration:none}

.hero{position:absolute;left:0;top:0;width:1200px;height:676px;background:linear-gradient(180deg,#6f7a5e 0%,#4f6a34 35%,#4c6d28 60%,#5f7f3a 100%)}
.hero-shade{position:absolute;inset:0;background:rgba(0,0,0,.22)}
.hero .brand{top:28px;color:var(--white)}
.hero .brand-square{background:var(--yellow)}
.hero .nav{height:85px}
.hero .nav a{color:#e8e8e8}
.hero .nav a.active{color:var(--yellow)}
.hero-title{position:absolute;top:250px;left:0;width:1200px;text-align:center;color:var(--white);font-size:60px;font-weight:700;line-height:68px}
.hero-sub{position:absolute;top:408px;left:0;width:1200px;text-align:center;color:var(--white);font-size:17px}
.btn{position:absolute;background:var(--yellow);color:var(--white);font-size:15px;font-weight:600;text-transform:uppercase;display:flex;align-items:center;justify-content:center;letter-spacing:.5px;border-bottom:3px solid var(--yellow-dark);text-decoration:none}

.navband{position:absolute;left:0;width:1200px;height:79px;background:var(--yellow);border-bottom:5px solid var(--yellow-dark)}
.navband .brand{top:22px;color:var(--ink)}
.navband .brand-square{background:var(--ink)}
.navband .nav a{color:var(--nav-muted)}
.navband .nav a.active{color:var(--white)}

/* headings */
.section-title{position:absolute;left:0;width:1200px;text-align:center;font-size:36px;color:var(--ink);font-weight:400}
.rule{position:absolute;height:3px;width:60px;background:var(--yellow)}
.lead{position:absolute;left:0;width:1200px;text-align:center;font-size:16px;color:var(--body)}

/* about */
.about-title{left:57px;top:880px;font-size:36px;color:var(--ink)}
.about-copy{left:57px;top:973px;width:345px;font-size:15px;line-height:25px}
.about-photo{left:450px;top:841px;width:291px;height:393px;background:var(--white);padding:8px;box-shadow:0 2px 14px rgba(0,0,0,.2)}
.about-photo div{width:100%;height:100%;background:linear-gradient(160deg,#2f7a22,#4fa732 50%,#2f6a1d)}
.side-title{left:790px;font-size:21px;color:var(--ink)}
.side-copy{left:790px;width:330px;font-size:15px;line-height:25px}

/* services */
.card-img{position:absolute;width:320px;height:200px}
.card-title{position:absolute;width:320px;font-size:17px;font-weight:600;color:var(--ink);text-transform:uppercase;line-height:23px}
.card-text{position:absolute;width:320px;font-size:15px;line-height:23px}

/* reviews */
.reviews-note{position:absolute;left:300px;width:600px;text-align:center;font-size:16px;line-height:26px;color:var(--body)}

/* quote band */
.quote{position:absolute;left:0;top:3121px;width:1200px;height:208px;background:linear-gradient(90deg,#3d3a36,#5a544c 55%,#6b5f52)}
.quote-text{position:absolute;left:0;top:3198px;width:1200px;text-align:center;color:var(--white);font-size:35px;line-height:48px}
.quote-text b{font-weight:700}

/* contact */
.field{position:absolute;border:1px solid var(--line);font-size:13px;color:#999;padding:6px 10px}
.info-col{position:absolute;top:3885px;width:260px;text-align:center;font-size:15px;line-height:31px;color:var(--body)}
.info-col h4{font-size:15px;font-weight:600;color:var(--ink);text-transform:uppercase;margin-bottom:14px}
.info-col svg{vertical-align:-2px;margin-right:6px}

.footer{position:absolute;left:0;top:4084px;width:1200px;height:192px;background:var(--footer)}
.social{position:absolute;top:4121px;width:40px;height:40px;border-radius:50%;background:#555}
.copyright{position:absolute;left:0;top:4208px;width:1200px;text-align:center;font-size:13px;color:#777}
</style>
</head>
<body>

<header class="hero">
  <div class="hero-shade" role="img" aria-label="Photo of a countryside estate with stone farmhouse, trees and flower borders"></div>
  <div class="brand"><span class="brand-square"></span>MARLOW LANDSCAPING</div>
  <nav class="nav"><a>About</a><a class="active">Services</a><a>Reviews</a><a>Contact</a></nav>
  <h1 class="hero-title">Dependable, Reliable &amp;<br>Consistent</h1>
  <p class="hero-sub">Hand Weeding, Landscaping &amp; Garden Services</p>
  <div class="btn" style="left:524px;top:493px;width:134px;height:46px">More Info</div>
</header>

<div class="navband" style="top:676px">
  <div class="brand"><span class="brand-square"></span>MARLOW LANDSCAPING</div>
  <nav class="nav"><a class="active">About</a><a>Services</a><a>Reviews</a><a>Contact</a></nav>
</div>

<section class="about">
  <h2 class="abs about-title" style="font-weight:400">What We Do</h2>
  <div class="rule" style="left:57px;top:941px"></div>
  <p class="abs about-copy">We are specialised in Weeding of Perennial and Flower Beds, Selective Pruning of Trees and Shrubs, Hedging, Landscape Construction, Landscape Design, Total Lawn Treatment Plans &amp; Landscape Pest Control.</p>
  <div class="btn" style="left:57px;top:1134px;width:157px;height:46px">Our Services</div>
  <div class="abs about-photo"><div role="img" aria-label="Close-up of a flower bed being hand weeded"></div></div>
  <h3 class="abs side-title" style="top:900px;font-weight:400">Who We Are</h3>
  <div class="rule" style="left:790px;top:945px"></div>
  <p class="abs side-copy" style="top:970px">Newyork Largest Landscaping company, we do landscaping, Hand weeding and gardening.</p>
  <h3 class="abs side-title" style="top:1040px;font-weight:400">Free Estimation</h3>
  <div class="rule" style="left:790px;top:1083px"></div>
  <p class="abs side-copy" style="top:1115px">We provide free estimation to our clients.</p>
</section>

<div class="navband" style="top:1348px">
  <div class="brand"><span class="brand-square"></span>MARLOW LANDSCAPING</div>
  <nav class="nav"><a>About</a><a class="active">Services</a><a>Reviews</a><a>Contact</a></nav>
</div>

<section class="services">
  <h2 class="section-title" style="top:1503px">Our Services</h2>
  <div class="rule" style="left:570px;top:1563px"></div>
  <p class="lead" style="top:1584px">We are providing wide range of services over gardening. We are specialised in below</p>

  <div class="card-img" style="left:68px;top:1693px;background:linear-gradient(160deg,#3f7d2a,#6aa23e 55%,#4f6c3a)" role="img" aria-label="Perennial flower bed being weeded"></div>
  <h3 class="card-title" style="left:68px;top:1912px">Weeding of Perennial and Flower Beds</h3>
  <div class="rule" style="left:68px;top:1965px"></div>
  <p class="card-text" style="left:68px;top:1980px">Lorem ipsum dolor sit amet, consectetur adipiscing elit. Duis sed dapibus leo nec ornare diam sedsed commodo nibh ante facilisis bibendum dolor feugiat at.</p>

  <div class="card-img" style="left:433px;top:1693px;background:linear-gradient(180deg,#8fb7d8,#5d8e4a 55%,#3e6a2a)" role="img" aria-label="Pruned trees and shrubs around a garden house"></div>
  <h3 class="card-title" style="left:433px;top:1912px">Selective Pruning of Trees and Shrubs</h3>
  <div class="rule" style="left:433px;top:1965px"></div>
  <p class="card-text" style="left:433px;top:1980px">Lorem ipsum dolor sit amet, consectetur adipiscing elit. Duis sed dapibus leo nec ornare diam sedsed commodo nibh ante facilisis bibendum dolor feugiat at.</p>

  <div class="card-img" style="left:798px;top:1693px;background:radial-gradient(circle at 40% 40%,#5fc46a,#1d7f3a 70%,#0f5428)" role="img" aria-label="Garden sprinkler watering a hedge"></div>
  <h3 class="card-title" style="left:798px;top:1912px">Hedging</h3>
  <div class="rule" style="left:798px;top:1942px"></div>
  <p class="card-text" style="left:798px;top:1957px">Lorem ipsum dolor sit amet, consectetur adipiscing elit. Duis sed dapibus leo nec ornare diam sedsed commodo nibh ante facilisis bibendum dolor feugiat at. Duis sed dapibus leo nec ornare diam sedsed commodo nibh ante facilisis bibendum dolor feugiat at.</p>

  <div class="card-img" style="left:68px;top:2166px;background:linear-gradient(160deg,#eef3e6,#a9cf6d 60%,#6e9a3b)" role="img" aria-label="Young seedlings growing in soil"></div>
  <h3 class="card-title" style="left:68px;top:2388px">Landscape Construction</h3>
  <div class="rule" style="left:68px;top:2418px"></div>
  <p class="card-text" style="left:68px;top:2433px">Lorem ipsum dolor sit amet, consectetur adipiscing elit. Duis sed dapibus leo nec ornare diam sedsed commodo nibh ante facilisis bibendum dolor feugiat at.</p>

  <div class="card-img" style="left:433px;top:2166px;background:linear-gradient(180deg,#7c9a4b,#5a6d35 50%,#3d4a26)" role="img" aria-label="Large old tree in a designed garden"></div>
  <h3 class="card-title" style="left:433px;top:2388px">Landscape Design</h3>
  <div class="rule" style="left:433px;top:2418px"></div>
  <p class="card-text" style="left:433px;top:2433px">Lorem ipsum dolor sit amet, consectetur adipiscing elit. Duis sed dapibus leo nec ornare diam sedsed commodo nibh ante facilisis bibendum dolor feugiat at.</p>

  <div class="card-img" style="left:798px;top:2166px;background:linear-gradient(180deg,#a8946b,#6f5a3c 50%,#4a4a2c)" role="img" aria-label="Tree-lined garden path in autumn"></div>
  <h3 class="card-title" style="left:798px;top:2388px">Total Lawn Treatment Plans &amp; Landscape Pest Control</h3>
  <div class="rule" style="left:798px;top:2441px"></div>
  <p class="card-text" style="left:798px;top:2456px">Lorem ipsum dolor sit amet, consectetur adipiscing elit. Duis sed dapibus leo nec ornare diam sedsed commodo nibh ante facilisis bibendum dolor feugiat at.</p>
</section>

<div class="navband" style="top:2556px">
  <div class="brand"><span class="brand-square"></span>MARLOW LANDSCAPING</div>
  <nav class="nav"><a>About</a><a>Services</a><a class="active">Reviews</a><a>Contact</a></nav>
</div>

<section class="reviews">
  <h2 class="section-title" style="top:2720px">Client Reviews</h2>
  <div class="rule" style="left:570px;top:2780px"></div>
  <p class="reviews-note" style="top:2808px">See what our clients say about us. Read honest reviews from real people on our Ratewell page.</p>
  <a class="btn" href="#ratewell" style="left:490px;top:2890px;width:220px;height:48px">Read Our Reviews</a>
</section>

<section class="quote" role="img" aria-label="Photo of a country house roofline under a dusky sky"></section>
<p class="quote-text">Get Your Free Quote Now. Call <b>204-731-4426</b></p>

<section class="contact">
  <h2 class="section-title" style="top:3418px">Contact Us</h2>
  <div class="rule" style="left:570px;top:3477px"></div>
  <p class="lead" style="top:3499px">Send your requirement we'll get back to you soon.</p>
  <div class="field" style="left:162px;top:3591px;width:414px;height:32px">Name</div>
  <div class="field" style="left:607px;top:3591px;width:413px;height:32px">Email</div>
  <div class="field" style="left:162px;top:3637px;width:858px;height:94px">Message</div>
  <div class="btn" style="left:499px;top:3765px;width:188px;height:48px">
    <svg width="14" height="14" viewBox="0 0 14 14" style="margin-right:6px"><path d="M1 7 L13 1 L9 13 L7 8 Z" fill="#fff"/></svg>Send Message
  </div>

  <div class="info-col" style="left:175px">
    <h4>Address</h4>
    Alder Row Street<br>New York, NY 10000
  </div>
  <div class="info-col" style="left:469px">
    <h4>Working Hours</h4>
    Monday-Saturday: 07:00 - 18:00<br>Sunday: CLOSED
  </div>
  <div class="info-col" style="left:721px;width:320px">
    <h4>Contact Info</h4>
    Gerald Hanswick<br>
    <svg width="13" height="13" viewBox="0 0 14 14"><path d="M3 1 L5 1 L6 4 L4.5 5.5 C5.5 7.5 6.5 8.5 8.5 9.5 L10 8 L13 9 L13 11 C13 12 12 13 11 13 C5.5 12.5 1.5 8.5 1 3 C1 2 2 1 3 1 Z" fill="#555"/></svg>: 204-731-4426<br>
    <svg width="13" height="11" viewBox="0 0 14 11"><rect x="0.5" y="0.5" width="13" height="10" fill="#555"/><path d="M0.5 0.5 L7 6 L13.5 0.5" stroke="#fff" fill="none"/></svg>: ger.hanswick@brelvanyard.com
  </div>
</section>

<footer class="footer"></footer>
<span class="social" style="left:533px"></span>
<span class="social" style="left:613px"></span>
<p class="copyright">Copyright © 2017 Marlow Landscaping. All Rights Reserved.</p>

</body>
</html>
```